Need a plumber

Would like a postcard sized flyer made up. Want the design to be kept very simple.
List of services we carry out in bullet point or similar.
Phone number and email included on the flyer.
Logo to feature prominantly.

List of services: Hot water issues
Burst Pipes
Gas Plumbing
Roof leaks
Drain blockages

Target Market(s)

Mums, dads and hosehgold owners

Industry/Entity Type

Plumbing

Colors
0054AA
0677BA
7BADD7
CADEEF
E8F1F8

Requirements
Must have
• Services we off and our logo, also must say "local plumber"

```html
<!DOCTYPE html>
<html lang="en">
<head>
<meta charset="utf-8">
<title>Need a plumber? – Clearwell Plumbing Solutions</title>
<link rel="stylesheet" href="https://fonts.googleapis.com/css2?family=Rubik:wght@600;700;800&family=Barlow+Condensed:wght@600&display=swap">
<style>
  :root {
    --ink-deep: #02070c;
    --ink-mid: #06223a;
    --water: #2a9fd6;
    --headline: #8fdcf7;
    --phone: #9fe3fb;
    --white: #ffffff;
  }
  * { margin: 0; padding: 0; box-sizing: border-box; }
  html, body { width: 800px; height: 1200px; overflow: hidden; background: var(--ink-deep); }
  .flyer {
    position: relative;
    width: 800px;
    height: 1200px;
    overflow: hidden;
    font-family: "Rubik", sans-serif;
    color: var(--white);
  }
  .hero-photo {
    position: absolute;
    inset: 0;
    background:
      radial-gradient(ellipse 32% 22% at 22% 76%, rgba(90,200,245,0.75), transparent 70%),
      radial-gradient(ellipse 14% 30% at 20% 52%, rgba(70,170,220,0.55), transparent 75%),
      radial-gradient(ellipse 18% 16% at 40% 46%, rgba(120,170,200,0.45), transparent 75%),
      radial-gradient(ellipse 20% 18% at 66% 52%, rgba(110,160,195,0.42), transparent 75%),
      radial-gradient(ellipse 30% 20% at 80% 62%, rgba(50,120,165,0.45), transparent 75%),
      radial-gradient(ellipse 60% 22% at 45% 80%, rgba(40,140,200,0.40), transparent 75%),
      linear-gradient(180deg, #0a1a26 0%, #0b2436 30%, #0d3a58 58%, #0a3350 75%, #041420 88%, var(--ink-deep) 100%);
  }
  .headline {
    position: absolute;
    top: 48px;
    left: 0;
    width: 100%;
    text-align: center;
    font-weight: 800;
    font-size: 122px;
    line-height: 128px;
    letter-spacing: -2px;
    color: var(--headline);
    text-shadow: 0 4px 10px rgba(0,0,0,0.55);
  }
  .tagline {
    position: absolute;
    top: 318px;
    left: 0;
    width: 100%;
    text-align: center;
    font-family: "Barlow Condensed", sans-serif;
    font-weight: 600;
    font-size: 32px;
    letter-spacing: 6px;
    text-transform: uppercase;
    color: var(--white);
    text-shadow: 0 2px 6px rgba(0,0,0,0.7);
  }
  .brand-badge {
    position: absolute;
    left: 240px;
    top: 550px;
    width: 320px;
    height: 320px;
  }
  .brand-badge svg { position: absolute; inset: 0; }
  .brand-name {
    position: absolute;
    inset: 0;
    display: flex;
    flex-direction: column;
    align-items: center;
    justify-content: center;
    text-align: center;
    font-weight: 600;
    font-size: 34px;
    line-height: 40px;
    letter-spacing: 3px;
    text-transform: uppercase;
    color: var(--white);
  }
  .services {
    position: absolute;
    top: 892px;
    left: 0;
    width: 100%;
    text-align: center;
    font-family: "Barlow Condensed", sans-serif;
    font-weight: 600;
    font-size: 35px;
    line-height: 48px;
    text-transform: uppercase;
    color: var(--white);
    text-shadow: 0 2px 6px rgba(0,0,0,0.6);
  }
  .services .dot { padding: 0 5px; }
  .phone {
    position: absolute;
    top: 1008px;
    left: 0;
    width: 100%;
    text-align: center;
    font-weight: 700;
    font-size: 62px;
    color: var(--phone);
    text-shadow: 0 3px 8px rgba(0,0,0,0.6);
  }
  .email {
    position: absolute;
    top: 1092px;
    left: 0;
    width: 100%;
    text-align: center;
    font-weight: 600;
    font-size: 25px;
    color: var(--white);
  }
</style>
</head>
<body>
  <main class="flyer">
    <div class="hero-photo" role="img" aria-label="Photo of a startled couple peering at a kitchen tap spraying water in a dark blue-lit kitchen"></div>

    <h1 class="headline">Need a<br>plumber?</h1>
    <p class="tagline">Your local plumber</p>

    <div class="brand-badge">
      <svg viewBox="0 0 320 320" aria-hidden="true">
        <circle cx="160" cy="160" r="154" fill="rgba(4,20,34,0.55)" stroke="var(--white)" stroke-width="6"/>
      </svg>
      <div class="brand-name">Clearwell<br>Plumbing<br>Solutions</div>
    </div>

    <p class="services">
      Hot water issues<span class="dot">•</span>Burst pipes<span class="dot">•</span>Gas plumbing<br>
      Roof leaks<span class="dot">•</span>Drain blockages
    </p>

    <p class="phone">+61 400 555 218</p>
    <p class="email">contact@domainname.com</p>
  </main>
</body>
</html>
```